New Product Packaging and Logo for Tamblin Spice

New Product Package Designs for Tamblin Spice with Logo Design

See through design
Big Bold text - including brand name Tamblin Spice
New Logo (which will need to be updated as part of this project)
Picture of Cinnamon
Flavour Profile (see breif.doc for info on this)
Ingredients - info on back
Front and Back design for both Pouch and Plastic Tube
Organic Cerifications
Descriptions of Smell/Flavour
More info on back - website, text (see brief.doc)
Bar Codes
Social Media references on back

Please see all info on Designbrief.doc

Target Market(s)

Households, cafes

Industry/Entity Type

Wholesale

Logo Text

Tamblin Spice - Only from Ceylon

Colors

Designer to choose colors to be used in the design.

Requirements
Must have
• See above
Nice to have
• See above
Should not have
• Any pictures using Cassia variety of cinnamon

```html
<!DOCTYPE html>
<html lang="en">
<head>
<meta charset="utf-8">
<title>Tamblin Spice – Ceylon Cinnamon Powder Pouch</title>
<link href="https://fonts.googleapis.com/css2?family=Jost:wght@400&family=Questrial&family=Tinos&display=swap" rel="stylesheet">
<style>
  :root {
    --backdrop: #e6e7ea;
    --pouch: #fafafa;
    --band-line: #8a4a12;
    --brand-brown: #7a3d0c;
    --accent-orange: #ec9a3c;
    --text-dark: #2b2b2b;
    --text-mid: #4a4a4a;
    --spice-light: #c48a5a;
    --spice-dark: #7b4a2a;
    --badge-white: #ffffff;
  }
  * { margin: 0; padding: 0; box-sizing: border-box; }
  html, body { width: 1200px; height: 1200px; overflow: hidden; background: var(--backdrop); }
  .stage { position: relative; width: 1200px; height: 1200px; }

  .pouch {
    position: absolute; left: 278px; top: 134px; width: 644px; height: 932px;
    background: var(--pouch);
    clip-path: polygon(18px 0, 626px 0, 644px 18px, 644px 932px, 0 932px, 0 18px);
    overflow: hidden;
  }
  .band-line { position: absolute; top: 0; bottom: 0; width: 3px; background: var(--band-line); }
  .band-line--left { left: 118px; }
  .band-line--right { left: 520px; }

  .hang-hole {
    position: absolute; left: 277px; top: 44px; width: 86px; height: 18px;
    border-radius: 9px; background: #f0f0f0; box-shadow: inset 0 1px 2px rgba(0,0,0,0.15);
  }

  .centre-column { position: absolute; left: 121px; width: 399px; text-align: center; }

  .brand-mark {
    position: absolute; left: 270px; top: 120px; width: 100px; height: 100px;
    border: 10px solid var(--accent-orange); border-radius: 50%;
  }
  .brand-name {
    top: 232px; font-family: "Jost", sans-serif; font-size: 42px; font-weight: 400;
    color: var(--brand-brown); letter-spacing: 1px;
  }
  .product-claim {
    top: 322px; font-family: "Questrial", sans-serif; font-size: 20px; color: var(--text-dark);
  }
  .product-type {
    top: 347px; font-family: "Questrial", sans-serif; font-size: 17px; color: var(--text-mid);
  }
  .aroma-headline {
    top: 464px; font-family: "Questrial", sans-serif; font-size: 22px; color: var(--brand-brown);
    letter-spacing: 0.5px;
  }
  .flavour-notes {
    top: 526px; font-family: "Questrial", sans-serif; font-size: 21px; line-height: 25px;
    color: var(--brand-brown);
  }

  .spice-photo {
    position: absolute; left: 121px; top: 638px; width: 399px; height: 294px;
    background: linear-gradient(180deg, rgba(250,250,250,0) 0%, var(--spice-light) 22%, #a76c42 55%, var(--spice-dark) 100%);
  }
  .spice-divider { position: absolute; left: 121px; top: 818px; width: 399px; height: 30px; }

  .cert-badges { position: absolute; left: 121px; top: 838px; width: 399px; display: flex; justify-content: center; gap: 24px; }
  .cert-badge {
    width: 56px; height: 56px; border-radius: 50%; background: var(--spice-dark);
    border: 4px solid var(--badge-white);
  }
  .net-weight {
    top: 900px; font-family: "Tinos", serif; font-size: 22px; color: var(--badge-white);
  }
</style>
</head>
<body>
<div class="stage">
  <div class="pouch">
    <div class="band-line band-line--left"></div>
    <div class="band-line band-line--right"></div>
    <div class="hang-hole"></div>

    <div class="brand-mark"></div>
    <p class="centre-column brand-name">Tamblin Spice</p>
    <p class="centre-column product-claim">100% Organic</p>
    <p class="centre-column product-type">Ceylon Cinnamon Powder</p>

    <p class="centre-column aroma-headline">MORE AROMATIC</p>
    <p class="centre-column flavour-notes">Naturally Sweet<br>Authentic<br>Cinnamon<br>Flavour</p>

    <div class="spice-photo" role="img" aria-label="Photograph of Ceylon cinnamon quills resting on a mound of ground cinnamon powder"></div>
    <svg class="spice-divider" viewBox="0 0 399 30" preserveAspectRatio="none" aria-hidden="true">
      <path d="M0 30 Q200 -8 399 30" fill="none" stroke="rgba(255,255,255,0.7)" stroke-width="2"/>
    </svg>

    <div class="cert-badges" aria-label="Certifications">
      <span class="cert-badge"></span>
      <span class="cert-badge"></span>
      <span class="cert-badge"></span>
      <span class="cert-badge"></span>
    </div>
    <p class="centre-column net-weight">150g</p>
  </div>
</div>
</body>
</html>
```